Sign Shop website

We need a web design for a sign company called Quanta Signs that builds signs for shops such as A Frames, Banners, Tennet Boards, Shop front windows etc...

The existing site is avaliable at www.quantasigns-demo.com.au

We will need to have a fresh makeover. The new site must have the following:

Photo Galleries (broken down into sections)
Store Locations (currently there are 4 stores)
Online quote form
List of services
About Us Page

We just need to front page designed in photoshop (the inner page is not necessary) We have a team that can code the site up.

The website should have the exact logo. Any person who alters the logo, design will be elimated.

No Twitter, RSS, LinkedIn icons

The main colours are yellow, black, blue, red

Target Market(s)

Any business

Industry/Entity Type

It Company

Requirements
Must have
• jQuery slider banner
Should not have
• Alter the logo in any way

```html
<!DOCTYPE html>
<html lang="en">
<head>
<meta charset="utf-8">
<title>Quanta Signs</title>
<link href="https://fonts.googleapis.com/css2?family=Roboto:wght@300;400;500;700&family=Roboto+Condensed:wght@400;700&display=swap" rel="stylesheet">
<style>
:root{
  --orange:#ff9433;
  --purple:#a0407a;
  --brand:#5a2d7a;
  --text:#555;
  --heading:#333;
  --light:#f2f2f2;
  --input:#f6f7ec;
}
*{box-sizing:border-box;margin:0;padding:0}
html,body{width:1075px;height:1200px;overflow:hidden;background:#fff;font-family:'Roboto',Arial,sans-serif;color:var(--text)}
.page{position:relative;width:1075px;height:1200px}
.abs{position:absolute}
.top-line{left:0;top:0;width:1075px;height:4px;background:var(--purple)}
.header{left:0;top:4px;width:1075px;height:120px;background:linear-gradient(#fff,#ececec)}
.brand{left:106px;top:44px;display:flex;align-items:center;gap:10px}
.brand-mark{width:34px;height:34px;background:var(--orange)}
.brand-name{font:700 30px 'Roboto',sans-serif;color:var(--brand)}
.nav a{position:absolute;top:49px;height:30px;font-family:'Roboto',sans-serif;font-size:13px;font-weight:400;line-height:30px;color:#777;text-decoration:none;text-transform:uppercase}
.nav .active{left:409px;width:74px;background:var(--orange);color:#fff;text-align:center;border-radius:3px}
.band{left:0;top:124px;width:1075px;height:416px;background:var(--orange)}
.slider{left:108px;top:152px;width:860px;height:359px;background:#fff;padding:5px}
.slide{width:100%;height:100%;background:linear-gradient(180deg,#6c7480 0%,#d4d6da 30%,#e6e7e9 50%,#6a82b8 62%,#c8cacd 78%,#8a8a8c 100%)}
.dots{left:128px;top:485px;display:flex;gap:6px}
.dots span{width:12px;height:12px;border-radius:50%;background:#fff}
.dots span:first-child{background:var(--orange)}
.welcome-title{left:108px;top:555px;font-family:'Roboto Condensed',sans-serif;font-size:21px;font-weight:400;line-height:26px;color:var(--heading)}
.welcome-rule{left:108px;top:588px;width:591px;height:1px;background:#ccc}
.welcome-photo{left:108px;top:604px;width:206px;height:213px;background:linear-gradient(160deg,#cfcfd2,#8e8e93 60%,#707075)}
.welcome-text{left:323px;top:602px;width:379px;font-family:'Roboto',sans-serif;font-size:10.4px;font-weight:300;line-height:17px;text-align:justify;color:#555}
.welcome-text p{margin-bottom:17px}
.enquiry{left:715px;top:550px;width:253px;height:274px;background:var(--orange);border:1px solid #f7b070}
.enquiry h2{position:absolute;left:10px;top:10px;font-family:'Roboto Condensed',sans-serif;font-size:17px;font-weight:400;line-height:20px;color:#fff}
.enquiry .sep{position:absolute;left:0;top:36px;width:100%;height:1px;background:#f7ae6a}
.field{position:absolute;left:15px;width:224px;height:27px;background:var(--input);border:1px solid #f9c593;font-family:'Roboto',sans-serif;font-size:11px;font-weight:300;line-height:13px;color:#888;padding:6px 8px}
.submit{position:absolute;left:167px;top:242px;width:70px;height:25px;background:#fff;color:var(--orange);font-family:'Roboto Condensed',sans-serif;font-size:14px;font-weight:700;text-align:center;line-height:25px}
.divider{left:108px;top:857px;width:860px;height:7px;border:1px solid #ccc;border-bottom:none;border-radius:4px 4px 0 0;background:linear-gradient(#e8e8e8,#fff)}
.section-title{top:885px;font-family:'Roboto Condensed',sans-serif;font-size:21px;font-weight:400;line-height:26px;color:var(--heading)}
.view-more{left:890px;top:886px;height:22px;border-left:1px solid #ddd;padding-left:9px;font-family:'Roboto Condensed',sans-serif;font-size:10px;font-weight:700;line-height:22px;color:var(--orange)}
.location{left:108px;width:268px;height:55px;background:linear-gradient(#fff,#ececec);border:1px solid #ddd;box-shadow:0 1px 2px rgba(0,0,0,.15)}
.location svg.pin{position:absolute;left:14px;top:15px}
.location span{position:absolute;left:53px;top:15px;font-family:'Roboto Condensed',sans-serif;font-size:21px;font-weight:400;line-height:24px;letter-spacing:1px;color:#444}
.location svg.chev{position:absolute;right:14px;top:23px}
.thumb{border:1px solid #ddd;background:#fff;padding:5px}
.thumb div{width:100%;height:100%}
.footer{left:0;top:1152px;width:1075px;height:48px;background:var(--light);text-align:center;font-family:'Roboto',sans-serif;font-size:12px;font-weight:400;line-height:56px;color:#555}
</style>
</head>
<body>
<div class="page">
  <div class="abs top-line"></div>
  <header class="abs header"></header>
  <div class="abs brand"><span class="brand-mark"></span><span class="brand-name">Quanta Signs</span></div>
  <nav class="nav">
    <a class="active">Home</a>
    <a style="left:509px">About Us</a>
    <a style="left:613px">Our Services</a>
    <a style="left:745px">Our Portfolio</a>
    <a style="left:883px">Contact Us</a>
  </nav>

  <div class="abs band"></div>
  <div class="abs slider"><div class="slide" role="img" aria-label="Photo of a white vehicle with blue signwriting graphics on its side"></div></div>
  <div class="abs dots"><span></span><span></span><span></span><span></span></div>

  <h1 class="abs welcome-title">Welcome!</h1>
  <div class="abs welcome-rule"></div>
  <div class="abs welcome-photo" role="img" aria-label="Photo of a small grey car with printed vehicle lettering"></div>
  <div class="abs welcome-text">
    <p>Quanta Signs is a Western Australian owned and managed company that was founded in 2005 and is fast becoming one of the state's leading manufacturer of quality signage.</p>
    <p>Supplying signage for any application. Vinyl Computer Cut Lettering, Large Format Digital Print, Photo quality, Banners, Roster signs, Pull up Displays, Vehicle and Shop Windows. From small stickers to large format just to name a few.</p>
    <p>Quanta Signs can take existing artwork and apply it to almost any medium. Or, if you need help designing your proposed signage, we have the expertise to help you with that too.It is the policy of Quanta Signs to endeavour always to provide to its customers only those products and services that meet their requirements.</p>
  </div>

  <form class="abs enquiry">
    <h2>QUICK ENQUIRY</h2>
    <div class="sep"></div>
    <div class="field" style="top:48px">Name:</div>
    <div class="field" style="top:89px">Email</div>
    <div class="field" style="top:129px">Phone</div>
    <div class="field" style="top:169px;height:63px">Message</div>
    <div class="submit">SUBMIT</div>
  </form>

  <div class="abs divider"></div>

  <h2 class="abs section-title" style="left:106px">OUR LOCATIONS</h2>
  <h2 class="abs section-title" style="left:401px">PHOTO GALLERY</h2>
  <div class="abs view-more">VIEW MORE &#9656;</div>

  <div class="abs location" style="top:932px">
    <svg class="pin" width="18" height="24" viewBox="0 0 18 24"><path d="M9 0a9 9 0 0 1 9 9c0 7-9 15-9 15S0 16 0 9a9 9 0 0 1 9-9z" fill="#ff9433"/><circle cx="9" cy="9" r="3.5" fill="#fff"/></svg>
    <span>WESTBROOK</span>
    <svg class="chev" width="16" height="10" viewBox="0 0 16 10"><path d="M2 2l6 6 6-6" stroke="#ccc" stroke-width="3" fill="none"/></svg>
  </div>
  <div class="abs location" style="top:1004px">
    <svg class="pin" width="18" height="24" viewBox="0 0 18 24"><path d="M9 0a9 9 0 0 1 9 9c0 7-9 15-9 15S0 16 0 9a9 9 0 0 1 9-9z" fill="#5a2d7a"/><circle cx="9" cy="9" r="3.5" fill="#fff"/></svg>
    <span>NORTHGATE</span>
    <svg class="chev" width="16" height="10" viewBox="0 0 16 10"><path d="M2 2l6 6 6-6" stroke="#ccc" stroke-width="3" fill="none"/></svg>
  </div>
  <div class="abs location" style="top:1077px">
    <svg class="pin" width="18" height="24" viewBox="0 0 18 24"><path d="M9 0a9 9 0 0 1 9 9c0 7-9 15-9 15S0 16 0 9a9 9 0 0 1 9-9z" fill="#e0457b"/><circle cx="9" cy="9" r="3.5" fill="#fff"/></svg>
    <span>LAKESIDE PARK</span>
    <svg class="chev" width="16" height="10" viewBox="0 0 16 10"><path d="M2 2l6 6 6-6" stroke="#ccc" stroke-width="3" fill="none"/></svg>
  </div>

  <div class="abs thumb" style="left:401px;top:932px;width:272px;height:209px"><div role="img" aria-label="Photo of a truck tailgate wrapped in colourful printed graphics" style="background:linear-gradient(135deg,#5a4a5a,#8a5a80 50%,#4a5a80)"></div></div>
  <div class="abs thumb" style="left:685px;top:932px;width:137px;height:101px"><div role="img" aria-label="Photo of a white station wagon with printed decals" style="background:linear-gradient(#c4ccd4,#dedede 55%,#a8a8a8)"></div></div>
  <div class="abs thumb" style="left:832px;top:932px;width:137px;height:101px"><div role="img" aria-label="Photo of a red vehicle with white graphics" style="background:linear-gradient(#c8a0a8,#c04050 55%,#8a3038)"></div></div>
  <div class="abs thumb" style="left:685px;top:1039px;width:137px;height:102px"><div role="img" aria-label="Photo of a blue car with green vehicle graphics" style="background:linear-gradient(135deg,#8aa4c4,#3a64a8 55%,#3a7a5a)"></div></div>
  <div class="abs thumb" style="left:832px;top:1039px;width:137px;height:102px"><div role="img" aria-label="Photo of a cream van with green signwriting" style="background:linear-gradient(#a8aea4,#e4e0d4 55%,#b8c0ac)"></div></div>

  <footer class="abs footer">&copy; 2013 Quanta Signs. All Rights Reserved.</footer>
</div>
</body>
</html>
```